New Business Card for Bright Harbor Builds

Need a business card the is more like a marketing promotion of our services
Must be horizontal orientation, One Sided Only, Max font size, Organize the Services
#1 General Contractor for Realtors
Remodels – Renovations – Repairs
Water & Mold Damage Experts
Painting: Interior/ Exterior
Flooring: Wood / LVT / Carpet
Plumbing: Repairs & Upgrades
Electric: Lights & Energy Efficient Upgrades
Kitchen & Bath Remodels
Fast Inspections Repair Billed Thru Escrow
BrightHarborBuilds.com
555-418-2796

Industry/Entity Type

General Contractor

Contact Information for Business Card

One Sided Only: #1 General Contractor for Realtors Remodels – Renovations – Repairs Water & Mold Damage Experts Painting: Interior/ Exterior Flooring: Wood / LVT / Carpet Plumbing: Repairs & Upgrades Electric: Lights & Energy Efficient Upgrades Kitchen & Bath Remodels Fast Inspections Repair Billed Thru Escrow BrightHarborBuilds.com 555-418-2796

Colors
0054AA
0677BA
7BADD7
CADEEF
E8F1F8

Requirements
Must have
• One Sided Only: #1 General Contractor for Realtors Remodels – Renovations – Repairs Water & Mold Damage Experts Painting: Interior/ Exterior Flooring: Wood / LVT / Carpet Plumbing: Repairs & Upgrades Electric: Lights & Energy Efficient Upgrades Kitchen & Bath Remodels Fast Inspections Repair Billed Thru Escrow BrightHarborBuilds.com 555-418-2796

```html
<!DOCTYPE html>
<html lang="en">
<head>
<meta charset="utf-8">
<title>Bright Harbor Builds – Business Card</title>
<link href="https://fonts.googleapis.com/css2?family=Montserrat:wght@400;500;700&display=swap" rel="stylesheet">
<style>
  :root {
    --navy: #233a66;
    --orange: #f28a1e;
    --white: #ffffff;
    --backdrop: #e6e6e6;
  }
  * { margin: 0; padding: 0; box-sizing: border-box; }
  html, body {
    width: 1200px;
    height: 849px;
    overflow: hidden;
    background: var(--backdrop);
    font-family: "Montserrat", Arial, sans-serif;
  }
  .card {
    position: absolute;
    left: 75px;
    top: 124px;
    width: 1050px;
    height: 600px;
    background: var(--white);
    overflow: hidden;
  }
  .card__waves {
    position: absolute;
    inset: 0;
    width: 100%;
    height: 100%;
  }
  .brand {
    position: absolute;
    left: 60px;
    top: 228px;
    width: 370px;
    display: flex;
    align-items: center;
    justify-content: center;
    gap: 12px;
  }
  .brand__dot {
    width: 34px;
    height: 34px;
    border-radius: 50%;
    background: var(--orange);
    flex: none;
  }
  .brand__name {
    font-weight: 700;
    font-size: 29px;
    letter-spacing: 0.5px;
    color: var(--navy);
    line-height: 1.1;
    text-transform: uppercase;
  }
  .services {
    position: absolute;
    right: 43px;
    top: 42px;
    list-style: none;
    text-align: right;
    color: var(--orange);
    font-weight: 500;
    font-size: 18px;
    line-height: 44px;
  }
  .contact {
    position: absolute;
    right: 43px;
    top: 458px;
    list-style: none;
    color: var(--orange);
    font-weight: 500;
    font-size: 20px;
  }
  .contact__item {
    display: flex;
    align-items: center;
    justify-content: flex-end;
    gap: 12px;
    height: 50px;
  }
  .contact__icon {
    width: 30px;
    height: 30px;
    border-radius: 50%;
    background: var(--orange);
    display: flex;
    align-items: center;
    justify-content: center;
    flex: none;
  }
  .contact__icon svg { width: 18px; height: 18px; }
</style>
</head>
<body>
  <main class="card">
    <svg class="card__waves" viewBox="0 0 687 393" preserveAspectRatio="none" aria-hidden="true">
      <path fill="var(--orange)" d="M240,0 C345,30 400,120 370,200 C345,265 290,300 285,340 C282,365 300,385 315,393 L687,393 L687,0 Z"/>
      <path fill="var(--white)" d="M275,0 C370,40 405,130 378,205 C355,265 305,300 300,340 C297,365 315,385 330,393 L687,393 L687,0 Z"/>
      <path fill="var(--navy)" d="M292,0 C385,45 415,135 385,210 C360,270 315,305 312,345 C310,370 330,388 345,393 L687,393 L687,0 Z"/>
      <path fill="var(--white)" d="M305,0 C395,55 422,140 392,215 C368,272 325,308 323,347 C322,372 342,388 355,393 L687,393 L687,0 Z"/>
      <path fill="var(--navy)" d="M318,0 C402,60 430,145 398,220 C374,276 334,312 333,350 C332,373 350,388 362,393 L687,393 L687,0 Z"/>
    </svg>

    <div class="brand">
      <span class="brand__dot"></span>
      <span class="brand__name">Bright Harbor Builds</span>
    </div>

    <ul class="services">
      <li>#1 General Contractor for Realtors</li>
      <li>Remodels – Renovations – Repairs</li>
      <li>Water &amp; Mold Damage Experts</li>
      <li>Painting: Interior/ Exterior</li>
      <li>Flooring: Wood / LVT / Carpet</li>
      <li>Plumbing: Repairs &amp; Upgrades</li>
      <li>Electric: Lights &amp; Energy Efficient Upgrades</li>
      <li>Kitchen &amp; Bath Remodels</li>
      <li>Fast Inspections Repair Billed Thru Escrow</li>
    </ul>

    <ul class="contact">
      <li class="contact__item">
        <span>BrightHarborBuilds.com</span>
        <span class="contact__icon">
          <svg viewBox="0 0 24 24" fill="none" stroke="var(--white)" stroke-width="1.8">
            <circle cx="12" cy="12" r="9"/>
            <ellipse cx="12" cy="12" rx="4" ry="9"/>
            <line x1="3" y1="12" x2="21" y2="12"/>
          </svg>
        </span>
      </li>
      <li class="contact__item">
        <span>555-418-2796</span>
        <span class="contact__icon">
          <svg viewBox="0 0 24 24" fill="var(--white)">
            <path d="M6.6 10.8a15 15 0 0 0 6.6 6.6l2.2-2.2c.3-.3.7-.4 1-.2 1.1.4 2.3.6 3.6.6.6 0 1 .4 1 1V20c0 .6-.4 1-1 1A17 17 0 0 1 3 4c0-.6.4-1 1-1h3.5c.6 0 1 .4 1 1 0 1.3.2 2.5.6 3.6.1.3 0 .7-.2 1z"/>
          </svg>
        </span>
      </li>
    </ul>
  </main>
</body>
</html>
```